Simple fencing and steel manufacturing website

** update 01/04/2015 ** we did not add logo design, but if your font/logo is accepted we will add $50 to make it more fair
Even if you web design is not chosen, but your logo is, we will pay you $50. If both are chosen you will get an extra $50
Open brief

Site map:
Home
About
Gallery
-photos
-testimonials
Contact

No current website:

No current logo, colors currently black and gold but we don't mind changing them - wide open brief
Happy for new font/style/logo for company name which is Paling Brightway

Customer wants clean, credible and professional look & feel
stock photos OK

Brief:

One home page - simple with 2 or 3 small areas to tease and attract the user and one template page to suit all the other pages

All competitor websites are pretty bad, the best of them is
http://www.wexmoorrailing.com.au/index.html

Target Market(s)

Government and top level builders

Industry/Entity Type

Fencing

Requirements
Must have
• 1. Display ISO and environmental awards (ISO9001 AS4801 ISO14001)
• 2. A list of about 15 products
• Can be in teaser areas of home page as suggested before or slider or really anywhere
Nice to have
• Log with name - nice but not necessary (we don't have one)

```html
<!DOCTYPE html>
<html lang="en">
<head>
<meta charset="utf-8">
<title>Paling Brightway – Fencing &amp; Steel</title>
<link rel="stylesheet" href="https://fonts.googleapis.com/css2?family=Roboto+Condensed:wght@400;700&family=Roboto:ital,wght@0,300;0,400;1,400&display=swap">
<style>
:root{
  --gold:#d9a100;
  --gold-band-top:#dca000;
  --gold-band-bottom:#f8bd08;
  --ink:#222;
  --text:#5a5a5a;
  --muted:#777;
  --rule:#b5b5b5;
  --footer:#2a2b2d;
  --footer-line:#4a4b4e;
  --white:#fff;
}
*{box-sizing:border-box;margin:0;padding:0}
html,body{width:1200px;height:1200px;overflow:hidden}
body{position:relative;background:linear-gradient(#e8e8ec 0,#f3f3f5 60%,#fafafa 100%);font-family:"Roboto",Arial,sans-serif;color:var(--text)}
.abs{position:absolute}
.gold-band{left:0;top:110px;width:1200px;height:301px;background:linear-gradient(var(--gold-band-top),var(--gold-band-bottom))}
.page{left:144px;top:0;width:917px;height:940px;background:var(--white);box-shadow:0 0 8px rgba(0,0,0,.45)}
/* header */
.brand{left:162px;top:56px;display:flex;align-items:center;gap:10px}
.brand-mark{width:22px;height:22px;background:var(--gold)}
.brand-name{font-family:"Roboto Condensed",sans-serif;font-weight:700;font-size:32px;letter-spacing:.5px;color:var(--ink);text-transform:uppercase}
.call{left:862px;top:18px;display:flex;align-items:center;gap:8px}
.call-label{font-family:"Roboto Condensed",sans-serif;font-size:15px;color:var(--ink);line-height:1}
.call-number{font-family:"Roboto Condensed",sans-serif;font-size:22px;color:var(--ink);line-height:1.1}
.nav{left:562px;top:70px;display:flex;align-items:center}
.nav a{font-family:"Roboto Condensed",sans-serif;font-size:14px;color:var(--gold);text-decoration:none;margin-left:25px;text-transform:uppercase}
.nav a.home{margin-left:0;margin-right:6px}
/* slider */
.slide-fence{left:144px;top:108px;width:604px;height:301px;background:linear-gradient(100deg,#3c4a2e 0%,#6f7b62 35%,#9aa08f 55%,#4e5848 80%,#2d3326 100%)}
.slide-couple{left:750px;top:108px;width:311px;height:301px;background:linear-gradient(160deg,#7a3b2c 0%,#a0604a 40%,#c9b7a8 60%,#3d3a3a 100%)}
.slide-divider{left:747px;top:108px;width:3px;height:301px;background:var(--gold)}
.caption{left:378px;top:374px;width:683px;height:35px;background:rgba(30,30,30,.72);display:flex;align-items:center;padding-left:7px}
.caption p{font-family:"Roboto Condensed",sans-serif;font-size:14.5px;color:var(--white)}
.dots{right:10px;top:12px;display:flex;gap:4px}
.dots span{width:11px;height:11px;border-radius:50%;background:var(--gold)}
.dots span.on{background:#ddd}
.inquiry{left:162px;top:135px;width:216px;height:274px;background:rgba(35,35,35,.82);padding:8px 6px}
.inquiry-title{display:flex;align-items:center;gap:8px;font-family:"Roboto Condensed",sans-serif;font-size:17px;color:var(--white);padding-bottom:6px;border-bottom:1px dashed #999;margin-bottom:12px}
.field{background:var(--white);border:1px solid #ccc;border-radius:2px;height:28px;margin-bottom:10px;font-size:11.5px;color:#555;padding:6px 10px;position:relative}
.field.select::after{content:"v";position:absolute;right:0;top:0;width:24px;height:26px;border-left:1px solid #ccc;text-align:center;line-height:26px;font-size:11px}
.field.message{height:80px}
.submit{display:inline-block;background:#8a8a8a;color:var(--white);font-family:"Roboto Slab",Georgia,serif;font-size:13px;padding:4px 11px;border-radius:2px}
/* content */
.section-title{font-family:"Roboto Condensed",sans-serif;font-size:17px;color:var(--ink);text-transform:uppercase;padding-bottom:6px;border-bottom:1px dashed var(--rule)}
.section-title em{font-style:normal;color:var(--gold)}
.body-copy{font-size:11.6px;line-height:18px;font-weight:300;color:var(--text);letter-spacing:.1px}
.more{font-size:12.5px;color:var(--ink);text-decoration:underline}
.welcome{left:179px;top:450px;width:542px}
.welcome .body-copy{margin-top:20px}
.welcome .body-copy+.body-copy{margin-top:18px}
.welcome .more{display:inline-block;margin-top:6px}
.col-divider{left:755px;top:447px;height:445px;border-left:1px dotted #bbb}
.testimonials{left:179px;top:718px;width:542px}
.quote{left:176px;top:757px;width:405px;font-size:11.6px;line-height:19.2px;color:#333;text-indent:32px}
.quote-open{left:180px;top:752px}
.quote-close{left:465px;top:858px}
.avatar{left:604px;top:761px;width:117px;height:117px;border-radius:50%;border:2px solid #9a6a2a;box-shadow:0 0 0 3px #eee;background:radial-gradient(circle at 50% 40%,#c9d6e2,#7d93a8)}
.avatar-name{left:615px;top:888px;font-size:12.5px;font-style:italic;color:#333}
.view-all{left:178px;top:908px}
.products{left:788px;top:450px;width:260px}
.products .body-copy{margin-top:12px}
.product-list{list-style:none;margin-top:8px}
.product-list li{font-size:12.4px;line-height:19.4px;font-weight:300;color:#444;padding-left:16px;position:relative}
.product-list li::before{content:"";position:absolute;left:1px;top:6px;border-left:5px solid var(--gold);border-top:4px solid transparent;border-bottom:4px solid transparent}
.products-more{left:989px;top:913px}
/* footer */
.footer{left:0;top:957px;width:1200px;height:177px;background:linear-gradient(#323335,#1f2022)}
.foot-title{font-family:"Roboto",sans-serif;font-size:13.5px;color:#eee;text-transform:uppercase;padding-bottom:8px;border-bottom:1px solid #111;box-shadow:0 1px 0 var(--footer-line)}
.quick{left:174px;top:975px;width:262px}
.links{left:172px;top:1004px;display:grid;grid-template-columns:116px 116px;column-gap:24px}
.links a{display:flex;align-items:center;gap:12px;height:28px;font-size:11.5px;color:#ddd;text-decoration:none;border-bottom:1px dotted #555;padding-left:10px}
.links a::before{content:"";border-left:5px solid #eee;border-top:4px solid transparent;border-bottom:4px solid transparent}
.v-rule{top:968px;height:145px;border-left:1px solid #111;box-shadow:1px 0 0 var(--footer-line)}
.contact{left:492px;top:975px;width:199px}
.contact-lines{left:494px;top:1015px;font-size:11.5px;line-height:16px;color:#eee}
.foot-brand{left:756px;top:990px;display:flex;align-items:center;gap:10px}
.foot-brand .brand-name{color:#f2f2f2;font-size:30px}
.badges{left:762px;top:1065px}
.copyright{left:0;top:1154px;width:1200px;text-align:center;font-size:13px;color:#555}
</style>
</head>
<body>
<div class="abs gold-band"></div>
<div class="abs page"></div>

<header>
  <div class="abs brand"><span class="brand-mark"></span><span class="brand-name">Paling Brightway</span></div>
  <div class="abs call">
    <svg width="30" height="30" viewBox="0 0 30 30"><circle cx="15" cy="15" r="13.5" fill="none" stroke="#d9a100" stroke-width="2"/><path d="M11 8c-2 1-2 4 0 8s5 7 8 7c1 0 2-1 2-2l-2-3-2 1c-1-1-3-3-4-5l1-2-2-4z" fill="#d9a100"/></svg>
    <div><div class="call-label">Call Us Today</div><div class="call-number">123-456-7890</div></div>
  </div>
  <nav class="abs nav">
    <a class="home" href="#" aria-label="Home"><svg width="26" height="24" viewBox="0 0 26 24"><path d="M13 1 1 12h3v11h6v-7h6v7h6V12h3z" fill="#111"/></svg></a>
    <a href="#">About Us</a><a href="#">Products</a><a href="#">Gallery</a><a href="#">Testimonials</a><a href="#">Contact Us</a>
  </nav>
</header>

<section class="slider">
  <div class="abs slide-fence" role="img" aria-label="Photo of an ornate black steel spear-top fence in front of garden greenery"></div>
  <div class="abs slide-divider"></div>
  <div class="abs slide-couple" role="img" aria-label="Photo of a smiling couple in front of a brick townhouse with a steel railing"></div>
  <div class="abs caption"><p>We Specialise in the supply &amp; installation of fencing for Government, Residential &amp; Commercial sectors</p>
    <div class="abs dots"><span></span><span class="on"></span><span></span><span></span></div></div>
  <form class="abs inquiry">
    <div class="inquiry-title"><svg width="24" height="16" viewBox="0 0 24 16"><rect x="1" y="1" width="22" height="14" fill="none" stroke="#fff" stroke-width="1.6"/><path d="M1 1l11 9 11-9" fill="none" stroke="#fff" stroke-width="1.6"/></svg>Quick Inquiry</div>
    <div class="field">Name</div>
    <div class="field">Email</div>
    <div class="field select">Inquiry For</div>
    <div class="field message">Message</div>
    <span class="submit">Submit</span>
  </form>
</section>

<main>
  <section class="abs welcome">
    <h2 class="section-title">Welcome to <em>Paling Brightway</em></h2>
    <p class="body-copy">Lorem ipsum dolor sit amet, consectetuer adipiscing elit, sed diam nonummy nibh euismod tincidunt ut laoreet dolore magna aliquam erat volutpat. Ut wisi enim ad minim veniam, quis nostrud exerci tation ullamcorper suscipit lobortis nisl ut aliquip ex ea commodo consequat. Duis autem vel eum iriure dolor in hendrerit in vulputate velit esse molestie consequat.</p>
    <p class="body-copy">Vel illum dolore eu feugiat nulla facilisis at vero eros et accumsan et iusto odio dignissim qui blandit praesent luptatum zzril delenit augue duis dolore te feugait nulla facilisi.Lorem ipsum dolor sit amet, consectetuer adipiscing elit, sed diam nonummy nibh euismod tincidunt ut laoreet dolore magna aliquam erat volutpat.</p>
    <a class="more" href="#">Read More</a>
  </section>

  <div class="abs col-divider"></div>

  <section class="abs testimonials"><h2 class="section-title">Client <em>Testimonials</em></h2></section>
  <svg class="abs quote-open" width="24" height="20" viewBox="0 0 24 20"><path d="M2 20V10c0-5 3-9 8-10v4c-2 1-3 3-3 5h3v11zM14 20V10c0-5 3-9 8-10v4c-2 1-3 3-3 5h3v11z" fill="#bbb"/></svg>
  <p class="abs quote">Lorem sum dolor sit amet, consectetuer adipiscing elit, sed diam nonummy nibh euismod tincidunt ut laoreet re agn aliqam erat volutpat wisi enim ad minim veniam, quis nostrud exerci tation ullamcorper suscipit lobortis nisl ut aliquip modo conseuatis autem vel eum iriure dolor in hendreritin hendrerit in vulputate velit esse molestie consequat, vel illum dolore eu im veniam, quis nostr im veniam, quis nostr</p>
  <svg class="abs quote-close" width="24" height="20" viewBox="0 0 24 20"><path d="M22 0v10c0 5-3 9-8 10v-4c2-1 3-3 3-5h-3V0zM10 0v10c0 5-3 9-8 10v-4c2-1 3-3 3-5H2V0z" fill="#bbb"/></svg>
  <div class="abs avatar" role="img" aria-label="Portrait photo of the client giving the testimonial"></div>
  <p class="abs avatar-name">Lorem ipsum, Dolor</p>
  <a class="abs more view-all" href="#">View All</a>

  <section class="abs products">
    <h2 class="section-title">Our <em>Products</em></h2>
    <p class="body-copy">Lorem ipsum dolor sit amet, consectetuer adipscing elit, sed diam nonummy nibh.</p>
    <ul class="product-list">
      <li>Eminence</li><li>Palisade (EA and IE Spec.)</li><li>Chainwire</li><li>Security Mesh (358 Mesh)</li><li>RTA Pedestrian (Type 1 - 5)</li><li>Partitions</li><li>Sporting Enclosures</li><li>Tubular (Pool/Garden)</li><li>Balustrades</li><li>Privacy Screens</li><li>Colourline Steel</li><li>Glass</li><li>Gates (Hinge)</li><li>Gates (Slide)</li><li>Boom Gates</li><li>Turnstiles</li><li>Bollards</li><li>Wheelstops</li><li>Guardrail</li>
    </ul>
  </section>
  <a class="abs more products-more" href="#">Read More</a>
</main>

<footer>
  <div class="abs footer"></div>
  <div class="abs quick"><h3 class="foot-title">Quick Links</h3></div>
  <nav class="abs links">
    <a href="#">Home</a><a href="#">Testimonials</a>
    <a href="#">About Us</a><a href="#">FAQ's</a>
    <a href="#">Products</a><a href="#">Contact Us</a>
    <a href="#">Gallery</a>
  </nav>
  <div class="abs v-rule" style="left:462px"></div>
  <div class="abs contact"><h3 class="foot-title">Contact Details</h3></div>
  <div class="abs contact-lines">Street Name City Name<br>State Zip Code<br><br>P : 123-456-7890<br><span style="display:block;margin-top:7px">Email : inquiry@palingbrightway.com</span></div>
  <div class="abs v-rule" style="left:729px"></div>
  <div class="abs foot-brand"><span class="brand-mark"></span><span class="brand-name">Paling Brightway</span></div>
  <svg class="abs badges" width="254" height="56" viewBox="0 0 254 56" role="img" aria-label="Quality, environmental and safety certification badges">
    <rect x="1" y="1" width="252" height="54" rx="27" fill="#3a3b3e" stroke="#bbb" stroke-width="2"/>
    <circle cx="28" cy="28" r="25" fill="#c8c8c8"/>
    <path d="M95 2a26 26 0 0 1 0 52M165 2a26 26 0 0 1 0 52" fill="none" stroke="#bbb" stroke-width="2"/>
  </svg>
  <p class="abs copyright">Copyright © 2015 PalingBrightway &nbsp;| &nbsp; All Rights Reserved &nbsp;| &nbsp; Terms &amp; Conditions</p>
</footer>
</body>
</html>
```